**Designs Wanted for High Profile Banner Ad Campaign**

Our leading Public Relations agency services some of the world's leading brands in our local market.

We now need a banner ad design to support our own growth.

We are looking to have banner ads designed that will carry a common theme to be used across the following sizes (all these sizes will need to be created):
• Vertical rectangle: 240 x 400
• Mobile leaderboard: 320 x 50
• Banner: 468 x 60
• Leaderboard: 728 x 90
• Square: 250 x 250
• Small square: 200 x 200
• Large rectangle: 336 x 280
• Inline rectangle: 300 x 250
• Skyscraper: 120 x 600
• Wide skyscraper: 160 x 600
• Half-page: 300 x 600
• Large leaderboard: 970x90
• Large mobile banner: 320 x 100
• Billboard: 970 x 250

Our primary retargeting and regular display campaign objective is to encourage marketing managers and business owners to visit our site and contact us.
See www.lumenvoicecomms.co.nz for our current look and feel. Please keep consistent colours with that site. Our two logos are attached.

This is our first digital retargeting campaign and we are open to your advice and suggestions on what will encourage click through from potential clients.

Our current thinking at the moment is that the ad could be built around these concepts:
“Reach, socialise, inspire.”
In others words – as a PR agency we help clients ‘reach’ their target market through creating content for news media.
The ‘socialise’ represents engagement through social media – in that we help develop and build their social media presence.
‘Inspire’ refers to the fact we aim to inspire their target market towards engaging with our clients.
Plus a suitable call to action– eg. Click here to meet your public relations needs today.

In terms of designs we are open to suggestion: eg. the adverts could use icons or something else that you have seen work.

We would like to see some eye catching animation, interaction or movement in the advert to.

We need the ad to be effective, eye catching, professional, modern, sophisticated (in that our target market is professional executives) and crisp, clean and uncluttered.

Time is short for us, so please send through designs as soon as possible – don’t wait until the last day!

Additional note: the existing fish image and 'stand out from the crowd' slogan on our home page are not required as part of this design. We have been looking to move towards the new slogan (“Reach, socialise, inspire.” ) and this banner ad may also serve to give us some new direction ideas as well. we do need to keep the existing logo and orange colour though.

Target Market(s)

Business to Business. Marketing and brand managers, Small, Medium and large business owners and executives.
Those with a business in the New Zealand market.

Industry/Entity Type

Marketing

Requirements
Must have
• our logo
animation or movement
orange colour/ consistency with our existing website.
our proposed slogan: “Reach, socialise, inspire.” (however we are open to seeing alternative ideas as well if you want to submit more than one concept)
call to action.
Should not have
• read note about existing fish and slogan above.

```html
<!DOCTYPE html>
<html lang="en">
<head>
<meta charset="utf-8">
<title>Lumen Voice – Display Banner Set</title>
<link rel="stylesheet" href="https://fonts.googleapis.com/css2?family=Arimo:ital,wght@0,400;0,700;1,400&display=swap">
<style>
  :root{
    --stage:#808080;
    --paper:#ffffff;
    --panel:#ececec;
    --ink:#1a1a1a;
    --brand-ink:#4d4d4d;
    --muted:#8f8f8f;
    --orange:#ff6600;
    --orange-text:#f26a1b;
    --photo-a:#d99a48;
    --photo-b:#6e4428;
    --photo-c:#f0b25a;
  }
  *{margin:0;padding:0;box-sizing:border-box}
  html,body{width:1200px;height:900px;overflow:hidden}
  body{position:relative;background:var(--stage);font-family:"Arimo",Arial,sans-serif;color:var(--ink)}

  .brand-strip{position:absolute;left:0;top:0;width:193px;height:900px;background:var(--paper)}
  .brand-strip__name{position:absolute;left:100px;top:450px;transform:translate(-50%,-50%) rotate(-90deg);
    white-space:nowrap;font-size:112px;font-weight:400;letter-spacing:8px;color:var(--brand-ink);line-height:1}

  .ad{position:absolute;background:var(--panel);overflow:hidden}
  .ad__header{position:absolute;left:0;right:0;top:0;background:var(--paper);box-shadow:0 4px 6px rgba(0,0,0,.12)}
  .wordmark{position:absolute;white-space:nowrap;font-weight:400;color:var(--brand-ink);letter-spacing:1.5px;line-height:1}
  .photo{position:absolute;background:
      radial-gradient(circle at 75% 30%,rgba(255,220,150,.55),transparent 35%),
      radial-gradient(circle at 15% 70%,rgba(255,200,120,.4),transparent 40%),
      linear-gradient(90deg,var(--photo-a),var(--photo-b) 45%,var(--photo-c))}
  .headline{position:absolute;white-space:nowrap;line-height:1}
  .headline em{font-style:normal;color:var(--orange-text)}
  .pillars{position:absolute;display:flex;gap:12px;white-space:nowrap;font-style:italic;color:var(--muted);line-height:1;list-style:none}
  .pillars--stack{flex-direction:column}
  .pillars li{display:flex;align-items:center;gap:5px}
  .tick{width:.8em;height:.8em;flex:none}
  .cta{position:absolute;background:var(--orange);color:#fff;font-weight:700;display:flex;align-items:center;justify-content:center;white-space:nowrap;text-transform:uppercase}
  .cta::after{content:"";position:absolute;left:50%;bottom:-5px;margin-left:-5px;border-left:5px solid transparent;border-right:5px solid transparent;border-top:5px solid var(--orange)}
  .tagline{position:absolute;font-style:italic;color:var(--muted);font-size:22px;line-height:32px;text-transform:uppercase}
</style>
</head>
<body>
<svg width="0" height="0" style="position:absolute">
  <symbol id="tick" viewBox="0 0 10 10"><path d="M1 5.2 L4 8 L9 1.5" fill="none" stroke="#ff6600" stroke-width="2" stroke-linecap="round" stroke-linejoin="round"/></symbol>
</svg>

<aside class="brand-strip"><div class="brand-strip__name">LUMENVOICE</div></aside>

<!-- Large leaderboard -->
<section class="ad" style="left:211px;top:26px;width:970px;height:90px">
  <div class="photo" role="img" aria-label="Photo of a smiling businessman against a warm blurred background" style="left:0;top:0;width:213px;height:90px"></div>
  <p class="headline" style="left:257px;top:18px;font-size:20px">Help build <em>consumer brands</em></p>
  <ul class="pillars" style="left:257px;top:51px;font-size:21px;gap:14px">
    <li><svg class="tick"><use href="#tick"/></svg>Reach</li>
    <li><svg class="tick"><use href="#tick"/></svg>Socialise</li>
    <li><svg class="tick"><use href="#tick"/></svg>Inspire</li>
  </ul>
  <span class="wordmark" style="right:134px;top:35px;font-size:23px">LUMENVOICE</span>
  <a class="cta" style="left:849px;top:29px;width:97px;height:38px;font-size:13px">Click here</a>
</section>

<!-- Large rectangle -->
<section class="ad" style="left:250px;top:150px;width:336px;height:280px">
  <div class="ad__header" style="height:60px"><span class="wordmark" style="left:17px;top:19px;font-size:25px">LUMENVOICE</span></div>
  <p class="headline" style="left:19px;top:79px;font-size:15px">Help build <em>consumer brands</em></p>
  <ul class="pillars" style="right:22px;top:110px;font-size:14px;gap:9px">
    <li><svg class="tick"><use href="#tick"/></svg>Reach</li>
    <li><svg class="tick"><use href="#tick"/></svg>Socialise</li>
    <li><svg class="tick"><use href="#tick"/></svg>Inspire</li>
  </ul>
  <div class="photo" role="img" aria-label="Photo of a smiling businessman against a warm blurred background" style="left:0;top:142px;width:336px;height:138px"></div>
  <a class="cta" style="left:228px;top:228px;width:87px;height:33px;font-size:12px">Click here</a>
</section>

<!-- Inline rectangle -->
<section class="ad" style="left:250px;top:488px;width:300px;height:250px">
  <div class="ad__header" style="height:50px"><span class="wordmark" style="left:12px;top:14px;font-size:23px">LUMENVOICE</span></div>
  <p class="headline" style="left:14px;top:67px;font-size:14px">Help build <em>consumer brands</em></p>
  <ul class="pillars" style="right:13px;top:96px;font-size:13px;gap:8px">
    <li><svg class="tick"><use href="#tick"/></svg>Reach</li>
    <li><svg class="tick"><use href="#tick"/></svg>Socialise</li>
    <li><svg class="tick"><use href="#tick"/></svg>Inspire</li>
  </ul>
  <div class="photo" role="img" aria-label="Photo of a smiling businessman against a warm blurred background" style="left:0;top:121px;width:300px;height:129px"></div>
  <a class="cta" style="left:207px;top:203px;width:80px;height:32px;font-size:11px">Click here</a>
</section>

<!-- Half page -->
<section class="ad" style="left:632px;top:146px;width:300px;height:600px">
  <div class="ad__header" style="height:57px;box-shadow:none"><span class="wordmark" style="left:18px;top:18px;font-size:26px">LUMENVOICE</span></div>
  <div class="photo" role="img" aria-label="Portrait photo of a smiling businessman against a warm blurred background" style="left:0;top:57px;width:300px;height:220px"></div>
  <div style="position:absolute;left:0;top:277px;width:300px;height:3px;background:var(--paper)"></div>
  <p class="headline" style="left:15px;top:302px;font-size:17px">Help build <em>consumer brands</em></p>
  <p class="tagline" style="left:15px;top:337px">Your best value<br>marketing options</p>
  <ul class="pillars pillars--stack" style="left:15px;top:429px;font-size:18px;gap:19px">
    <li><svg class="tick"><use href="#tick"/></svg>Reach</li>
    <li><svg class="tick"><use href="#tick"/></svg>Socialise</li>
    <li><svg class="tick"><use href="#tick"/></svg>Inspire</li>
  </ul>
  <a class="cta" style="left:174px;top:535px;width:103px;height:39px;font-size:14px">Click here</a>
</section>

<!-- Wide skyscraper -->
<section class="ad" style="left:978px;top:146px;width:160px;height:600px">
  <div class="ad__header" style="height:109px">
    <span class="wordmark" style="left:0;right:0;top:20px;text-align:center;font-size:22px">LUMEN</span>
    <span class="wordmark" style="left:0;right:0;top:48px;text-align:center;font-size:22px">VOICE</span>
  </div>
  <p class="headline" style="left:38px;top:140px;font-size:15px">Help build</p>
  <p class="headline" style="left:14px;top:169px;font-size:15px"><em>consumer brands</em></p>
  <ul class="pillars pillars--stack" style="left:37px;top:205px;font-size:15px;gap:15px">
    <li><svg class="tick"><use href="#tick"/></svg>Reach</li>
    <li><svg class="tick"><use href="#tick"/></svg>Socialise</li>
    <li><svg class="tick"><use href="#tick"/></svg>Inspire</li>
  </ul>
  <a class="cta" style="left:36px;top:329px;width:87px;height:33px;font-size:12px">Click here</a>
  <div class="photo" role="img" aria-label="Portrait photo of a smiling businessman against a warm blurred background" style="left:0;top:381px;width:160px;height:219px"></div>
</section>

<!-- Leaderboard -->
<section class="ad" style="left:250px;top:777px;width:728px;height:90px">
  <div class="photo" role="img" aria-label="Photo of a smiling businessman against a warm blurred background" style="left:0;top:0;width:205px;height:90px"></div>
  <p class="headline" style="left:236px;top:24px;font-size:17px">Help build <em>consumer brands</em></p>
  <ul class="pillars" style="left:340px;top:53px;font-size:15px;gap:9px">
    <li><svg class="tick"><use href="#tick"/></svg>Reach</li>
    <li><svg class="tick"><use href="#tick"/></svg>Socialise</li>
    <li><svg class="tick"><use href="#tick"/></svg>Inspire</li>
  </ul>
  <span class="wordmark" style="right:18px;top:17px;font-size:16px;letter-spacing:1px">LUMENVOICE</span>
  <a class="cta" style="left:599px;top:44px;width:111px;height:34px;font-size:14px">Click here</a>
</section>
</body>
</html>
```